New, modern business card for growing audiology practice

We need a new business card for our audiology practice. Our logo and website have recently changed (more modern) and we want our business cards to reflect this change.
We conduct hearing tests, perform earwax removals, and fit & dispense hearing aids to our patients. We are a family owned practice in which the owner is the one who works directly with the patient. I have attached logos in various formats to use, as well as two ideas I found on this website; as well as a scanned copy of our current logo. Good luck!

Industry/Entity Type

Business

Contact Information for Business Card

Company name: Maplow Hearing Center
Provider name: Peter Mulvoy, Au.D. F/ISN
Phone number: (555) 318-6042
Address: 87 W. Linden Ave. Alderton Falls, OH 43190
email: maplowhearing@postvale.net
website: maplowhearing.com

Colors
000000
aaaaaa
dbdbdb
cacaca
9bcb3c
afd23c
cadf82
b1b1b1

Requirements
Must have
• My card must include information in the "details" section. In the attached images, I found a few that I liked and I would like to model after - "brisk tumblin'" and "Sound Wellness Center".
• Must be horizontal.
• Must include logos provided. I uploaded them in various file formats and various ways.
• Must match logo font, if possible, if not, please get as close as you can.
Nice to have
• I really like the idea of having a color on one side with just the logo and company name and the contact information and provider name on the other side. I also really like the idea of having the main color dominating on the logo/company side with accent of that same color on the contact side of the card.
Should not have
• Must not be vertical.

```html
<!DOCTYPE html>
<html lang="en">
<head>
<meta charset="utf-8">
<title>Maplow Hearing Center – Business Card</title>
<link rel="stylesheet" href="https://fonts.googleapis.com/css2?family=Lato:wght@400&family=Roboto:wght@400&family=Roboto+Condensed:wght@500;700&display=swap">
<style>
  :root {
    --backdrop: #ece8e2;
    --card-dark: #1a1b1d;
    --card-light: #f4f4f3;
    --brand-green: #7aa43f;
    --ink: #151515;
    --ink-soft: #4a4a4a;
    --white: #ffffff;
  }
  * { box-sizing: border-box; margin: 0; padding: 0; }
  html, body { width: 1200px; height: 960px; overflow: hidden; }
  body { background: var(--backdrop); position: relative; }

  .card {
    position: absolute;
    width: 600px;
    height: 344px;
    border-radius: 20px;
    overflow: hidden;
  }

  /* Front */
  .card-front { left: 322px; top: 106px; background: var(--card-dark); }
  .brand {
    display: flex;
    align-items: center;
    gap: 12px;
    font-family: "Lato", sans-serif;
    font-weight: 400;
    text-transform: uppercase;
    white-space: nowrap;
  }
  .brand-dot {
    flex: none;
    border-radius: 50%;
    background: var(--brand-green);
  }
  .card-front .brand {
    position: absolute;
    left: 92px; top: 154px;
    font-size: 29px;
    color: var(--white);
    letter-spacing: 0.2px;
  }
  .card-front .brand-dot { width: 22px; height: 22px; }
  .front-url {
    position: absolute;
    left: 0; right: 0; top: 288px;
    text-align: center;
    font-family: "Roboto", sans-serif;
    font-size: 14px;
    letter-spacing: 3.6px;
    color: var(--white);
  }

  /* Back */
  .card-back { left: 320px; top: 493px; background: var(--card-light); }
  .name-band {
    position: absolute;
    left: 62px; right: 0; top: 42px;
    height: 56px;
    background: var(--brand-green);
    display: flex;
    align-items: center;
    padding-left: 130px;
    font-family: "Roboto Condensed", sans-serif;
    color: var(--white);
  }
  .name-band .band-circle {
    position: absolute;
    left: -6px; top: 3px;
    width: 50px; height: 50px;
    border-radius: 50%;
    background: var(--card-light);
    border: 6px solid var(--brand-green);
  }
  .provider-name { font-size: 22px; font-weight: 700; text-transform: uppercase; }
  .provider-sep { font-size: 22px; font-weight: 500; margin: 0 6px; }
  .provider-title { font-size: 15px; font-weight: 500; letter-spacing: 0.4px; padding-top: 2px; }

  .card-back .brand {
    position: absolute;
    right: 32px; top: 144px;
    font-size: 22px;
    color: var(--ink);
    gap: 10px;
  }
  .card-back .brand-dot { width: 16px; height: 16px; }

  .address, .contacts {
    position: absolute;
    right: 28px;
    text-align: right;
    font-family: "Roboto", sans-serif;
    font-size: 14.5px;
    line-height: 19px;
    color: var(--ink-soft);
  }
  .address { top: 206px; font-style: normal; }
  .contacts { top: 253px; list-style: none; right: 30px; }
  .contacts li { display: flex; align-items: center; justify-content: flex-end; gap: 12px; height: 19px; }
  .contacts svg { width: 13px; height: 13px; flex: none; fill: var(--brand-green); }
</style>
</head>
<body>

<section class="card card-front" aria-label="Business card front">
  <div class="brand"><span class="brand-dot"></span>Maplow Hearing Center</div>
  <p class="front-url">www.maplowhearing.com</p>
</section>

<section class="card card-back" aria-label="Business card back">
  <div class="name-band">
    <span class="band-circle"></span>
    <span class="provider-name">Peter Mulvoy</span>
    <span class="provider-sep">|</span>
    <span class="provider-title">AU.D. F/ISN</span>
  </div>

  <div class="brand"><span class="brand-dot"></span>Maplow Hearing Center</div>

  <address class="address">
    87 W. Linden Ave.<br>
    Alderton Falls, OH 43190
  </address>

  <ul class="contacts">
    <li>(555) 318-6042
      <svg viewBox="0 0 24 24" aria-hidden="true"><path d="M6.6 10.8a15.1 15.1 0 0 0 6.6 6.6l2.2-2.2c.3-.3.7-.4 1-.2 1.1.4 2.3.6 3.6.6.6 0 1 .4 1 1V20c0 .6-.4 1-1 1A17 17 0 0 1 3 4c0-.6.4-1 1-1h3.5c.6 0 1 .4 1 1 0 1.3.2 2.5.6 3.6.1.3 0 .7-.2 1z"/></svg>
    </li>
    <li>maplowhearing@postvale.net
      <svg viewBox="0 0 24 24" aria-hidden="true"><path d="M2 5h20v14H2z"/><path d="M2 5l10 7.5L22 5v2l-10 7.5L2 7z" fill="#f4f4f3"/></svg>
    </li>
    <li>maplowhearing.com
      <svg viewBox="0 0 24 24" aria-hidden="true"><circle cx="12" cy="12" r="11"/><path d="M8 6c2 1 3 3 2 5s1 3 3 3 2 3 0 5M15 4c-1 2 1 3 3 3" stroke="#f4f4f3" stroke-width="2" fill="none"/></svg>
    </li>
  </ul>
</section>

</body>
</html>
```